Harbor Crestline (Business Card Design)

Need business cards designed. Something modern, chic, and sleek. Mabye the back of the card should be the navy blue that is in the logo and then just the logo on the back.

Target Market(s)

Those in the hotel, office, and renovation industry

Contact Information for Business Card

1. Logo 2. Tomasz Ferreiro 3. CEO/Founder 4. Phone: (833) HarbCre / (833) 427-2273 5. Email: tomasz@theharborcrestline.com 6. Website: www.theharborcrestline.com

Font styles to use
Other font styles liked:
• Look at the logo font and base the font for everything else off of that.

Colors
0054AA
0677BA
7BADD7
CADEEF
E8F1F8

Requirements
Must have
• Colors that are associated in the logo
Nice to have
• Sleek modern clean and chic design.

```html
<!DOCTYPE html>
<html lang="en">
<head>
<meta charset="utf-8">
<title>Harbor Crestline — Business Card</title>
<link rel="stylesheet" href="https://fonts.googleapis.com/css2?family=Open+Sans:wght@400;600;700&display=swap">
<style>
  :root {
    --backdrop: #2a2b2e;
    --navy: #0c1642;
    --navy-deep: #080f33;
    --navy-soft: #1a2766;
    --gold: #c9a23a;
    --white: #ffffff;
  }
  * { box-sizing: border-box; margin: 0; padding: 0; }
  html, body {
    width: 1200px; height: 780px; overflow: hidden;
    background: var(--backdrop);
    font-family: "Open Sans", Arial, sans-serif;
  }
  .canvas {
    width: 1200px; height: 780px;
    display: flex; align-items: center; justify-content: center; gap: 40px;
  }
  .card {
    position: relative;
    width: 540px; height: 308px;
    background: var(--navy);
    overflow: hidden;
    box-shadow: 0 18px 40px rgba(0,0,0,.45);
  }

  /* Front */
  .mark-decor {
    position: absolute; left: 290px; top: 196px;
    width: 180px; height: 112px;
    background: linear-gradient(120deg, var(--navy-deep) 0%, var(--navy-soft) 60%, #5a5f9c 100%);
    opacity: .6;
    z-index: 0;
  }
  .brand, .address, .contacts, .person, .accent-bar { z-index: 1; }
  .brand {
    position: absolute; left: 30px; top: 30px;
    display: flex; align-items: center; gap: 12px;
  }
  .brand-square {
    width: 26px; height: 26px; background: var(--white);
  }
  .brand-name {
    color: var(--white); font-weight: 600; font-size: 17px;
    letter-spacing: 2px; text-transform: uppercase;
  }
  .address {
    position: absolute; left: 30px; top: 92px;
    color: var(--white); font-size: 13px; line-height: 19px; font-style: normal;
  }
  .contacts {
    position: absolute; left: 30px; top: 150px;
    list-style: none; color: var(--white); font-size: 12.5px;
  }
  .contacts li {
    display: flex; align-items: center; gap: 9px; line-height: 22px;
    white-space: nowrap;
  }
  .contacts svg { width: 13px; height: 13px; flex: none; }
  .person {
    position: absolute; right: 44px; top: 118px; text-align: right;
  }
  .person-name {
    color: var(--gold); font-weight: 700; font-size: 27px; line-height: 32px;
    white-space: nowrap;
  }
  .person-title {
    color: var(--white); font-size: 15px; margin-top: 2px;
  }
  .accent-bar {
    position: absolute; right: 0; top: 122px;
    width: 22px; height: 54px; background: var(--gold);
  }

  /* Back */
  .back-pattern {
    position: absolute; inset: 0;
    background: linear-gradient(135deg, var(--navy-deep) 0%, var(--navy) 55%, #3a4486 100%);
  }
  .back-brand {
    position: absolute; right: 34px; bottom: 30px;
    display: flex; align-items: center; gap: 9px;
  }
  .back-brand .brand-square { width: 16px; height: 16px; }
  .back-brand .brand-name { font-size: 11px; letter-spacing: 1.5px; }
</style>
</head>
<body>
<main class="canvas">

  <section class="card card-front" aria-label="Card front">
    <span class="mark-decor" role="img" aria-label="Large faint brand mark with a soft sheen"></span>

    <div class="brand">
      <span class="brand-square"></span>
      <span class="brand-name">Harbor Crestline</span>
    </div>

    <address class="address">
      4120 Meridian Park Way<br>
      Suite 210, Easton, MD 21601
    </address>

    <ul class="contacts">
      <li>
        <svg viewBox="0 0 24 24" fill="var(--gold)" aria-hidden="true"><path d="M6.6 10.8a15.1 15.1 0 0 0 6.6 6.6l2.2-2.2a1 1 0 0 1 1-.25 11.4 11.4 0 0 0 3.6.57 1 1 0 0 1 1 1V20a1 1 0 0 1-1 1A17 17 0 0 1 3 4a1 1 0 0 1 1-1h3.5a1 1 0 0 1 1 1c0 1.25.2 2.45.57 3.57a1 1 0 0 1-.25 1z"/></svg>
        (833) HarbCre / (833) 427-2273
      </li>
      <li>
        <svg viewBox="0 0 24 24" fill="none" stroke="var(--gold)" stroke-width="2" aria-hidden="true"><circle cx="12" cy="12" r="9"/><path d="M3 12h18M12 3c3 3.2 3 14.8 0 18M12 3c-3 3.2-3 14.8 0 18"/></svg>
        www.theharborcrestline.com
      </li>
      <li>
        <svg viewBox="0 0 24 24" fill="none" stroke="var(--gold)" stroke-width="2" aria-hidden="true"><rect x="3" y="5" width="18" height="14" rx="1"/><path d="M3 6l9 7 9-7"/></svg>
        tomasz@theharborcrestline.com
      </li>
    </ul>

    <div class="person">
      <p class="person-name">Tomasz Ferreiro</p>
      <p class="person-title">CEO/Founder</p>
    </div>
    <span class="accent-bar"></span>
  </section>

  <section class="card card-back" aria-label="Card back">
    <div class="back-pattern" role="img" aria-label="Repeating pattern of small brand marks on navy, fading to light at one corner"></div>
    <div class="back-brand">
      <span class="brand-square"></span>
      <span class="brand-name">Harbor Crestline</span>
    </div>
  </section>

</main>
</body>
</html>
```